Flyer-Design für Immobilienmakler
Zielgruppe
Wir sind Immobilienmakler und die Zielgruppe sind Immobilieneigentümer. Mit dem Flyer wollen wir kreative und evtl. auch 'freche' art auf uns aufmernksammachen, dass der Verkaufwillige sich an uns wendet.
Aufgabenstellung
Was wir nicht wollen: Flyer wie sie alle machen...ala wir sind die Tollsten und Besten.
Die Flyerform kann gerne besonders sein.
Unser Farben:
Blau R33 G49 B98
Rot R201 G0 B25
Unsere 'Wanda' und das Logo sende ich Ihnen als JPG.
Die Vektordatei reiche ich nach

```html
<!DOCTYPE html>
<html lang="de">
<head>
<meta charset="utf-8">
<title>Lumen Immobilien – Flyer</title>
<link href="https://fonts.googleapis.com/css2?family=Jost:wght@400;500;600&display=swap" rel="stylesheet">
<style>
:root{
  --blue:#352f63;
  --red:#c90019;
  --white:#ffffff;
  --ink:#2a2a2a;
  --photo-a:#6e6c69;
  --photo-b:#d8d4cf;
  --photo-c:#eceae8;
}
*{margin:0;padding:0;box-sizing:border-box}
html,body{width:1200px;height:1200px;overflow:hidden;background:#fff}
body{position:relative;font-family:'Jost',sans-serif;color:var(--ink)}
.panel{position:absolute;overflow:hidden;background:var(--white);box-shadow:2px 3px 5px rgba(0,0,0,.35)}
.cover-spread{left:32px;top:50px;width:756px;height:377px}
.cover-single{left:811px;top:50px;width:380px;height:377px}
.inside-spread{left:32px;top:542px;width:756px;height:378px}
.back-single{left:811px;top:542px;width:378px;height:378px;background:var(--blue)}
.bg-shapes{position:absolute;inset:0;width:100%;height:100%}
.brand-block{position:absolute;left:0;top:0;width:378px;color:var(--white);text-align:center}
.brand-name{position:absolute;top:32px;width:100%;font-size:18.5px;font-weight:500}
.brand-rule{position:absolute;top:67px;left:139px;width:100px;height:2px;background:var(--white)}
.slogan{position:absolute;top:80px;width:100%;font-size:18.5px;font-weight:600}
.office{position:absolute;top:165px;text-align:left;font-size:8.2px;line-height:9.8px;font-weight:400}
.office h3{font-size:7.8px;font-weight:600;letter-spacing:.2px;margin-bottom:10px}
.office p+p{margin-top:9px}
.office.main{left:45px}
.office.branch{left:207px}
.photo{position:absolute;background:linear-gradient(165deg,var(--photo-a) 0%,#a9a6a2 30%,var(--photo-b) 55%,var(--photo-c) 80%,#c5c2be 100%)}
.headline{position:absolute;right:37px;top:28px;display:flex;flex-direction:column;align-items:flex-end}
.headline .hook{display:block;background:var(--blue);color:var(--white);font-size:16px;font-weight:500;line-height:21.5px;padding:5px 11px 4px 10px;width:244px}
.headline .cta{display:block;background:var(--red);color:var(--white);font-size:15px;font-weight:600;letter-spacing:.2px;line-height:22px;padding:1px 9px 1px;white-space:nowrap;margin-right:-2px}
.wordmark{position:absolute;color:var(--blue);font-size:15px;font-weight:500;line-height:1;white-space:nowrap}
.columns{position:absolute;top:20px;font-size:9px;line-height:9.8px;width:164px}
.columns h4{color:var(--blue);font-size:8.4px;font-weight:400;margin-bottom:5px;text-transform:uppercase}
.columns p{margin-bottom:13px}
.col1{left:20px}.col2{left:194px}.col3{left:398px}.col4{left:572px}
</style>
</head>
<body>

<section class="panel cover-spread">
  <div class="photo" style="left:378px;top:0;width:378px;height:377px" role="img" aria-label="Foto: Person im weißen Hemd mit einem aufgeklappten Laptop über dem Kopf"></div>
  <svg class="bg-shapes" viewBox="0 0 756 377" preserveAspectRatio="none">
    <rect x="0" y="0" width="378" height="377" fill="var(--blue)"/>
    <polygon points="117,377 378,259 636,377" fill="var(--white)"/>
  </svg>
  <div class="brand-block">
    <div class="brand-name">Lumen Immobilien GmbH</div>
    <div class="brand-rule"></div>
    <div class="slogan">Besser wohnen – Besser leben!</div>
    <div class="office main">
      <h3>HAUPTGESCHÄFTSSTELLE NORDHEIM</h3>
      <p>Lumen Immobilien GmbH</p>
      <p>Lindenweg 7<br>21000 Nordheim<br>info@lumen-immobilien.example<br>Tel.&nbsp; +49 4100-1 23 45 60<br>Fax. +49 4100-1 23 45 61</p>
    </div>
    <div class="office branch">
      <h3>FILIALE SÜDHAFEN</h3>
      <p>Lumen Immobilien GmbH</p>
      <p>Hafenweg 35<br>21600 Südhafen<br>suedhafen@lumen-immobilien.example<br>Tel.&nbsp; +49 4160-9 87 65 40<br>Fax. +49 4160-9 87 65 41</p>
    </div>
  </div>
  <div class="headline">
    <span class="hook">Damit Ihnen der Haus verkauf nicht über den Kopf wächst.</span>
    <span class="cta">WIR BERATEN SIE GERNE!</span>
  </div>
  <div class="wordmark" style="left:398px;top:348px">Lumen Immobilien</div>
</section>

<section class="panel cover-single">
  <div class="photo" style="inset:0" role="img" aria-label="Foto: Person im weißen Hemd mit einem aufgeklappten Laptop über dem Kopf"></div>
  <svg class="bg-shapes" viewBox="0 0 380 377" preserveAspectRatio="none">
    <polygon points="0,259 0,377 258,377" fill="var(--white)"/>
  </svg>
  <div class="headline">
    <span class="hook">Damit Ihnen der Haus verkauf nicht über den Kopf wächst.</span>
    <span class="cta">WIR BERATEN SIE GERNE!</span>
  </div>
  <div class="wordmark" style="left:20px;top:348px">Lumen Immobilien</div>
</section>

<section class="panel inside-spread">
  <svg class="bg-shapes" viewBox="0 0 756 378" preserveAspectRatio="none">
    <polygon points="756,238 756,378 459,378" fill="var(--blue)"/>
    <polygon points="756,222 756,238 459,378 437,378" fill="var(--red)"/>
    <polygon points="0,171 425,378 0,378" fill="var(--blue)"/>
  </svg>
  <div class="photo" style="left:0;top:0;width:425px;height:378px;clip-path:polygon(0 185px,400px 378px,0 378px);background:linear-gradient(180deg,#8fb3dc 0%,#c9dcef 40%,#7f8a8c 65%,#3f5f7e 85%,#4c6a3a 100%)" role="img" aria-label="Foto: Paar umarmt sich vor einem modernen Einfamilienhaus"></div>
  <div class="photo" style="left:625px;top:232px;width:100px;height:146px;clip-path:ellipse(45% 50% at 50% 55%);background:linear-gradient(180deg,#c9a36a 0%,#e7d9c6 35%,#efe9df 60%,#5d6f8a 100%)" role="img" aria-label="Foto: lächelnde Frau hält ein Schild mit der Aufschrift SOLD"></div>
  <div class="columns col1">
    <h4>Lorem ipsum</h4>
    <p>Lorem ipsum dolor sit amet, consectetuer adipiscing elit. Aenean commodo ligula eget dolor. Aenean massa. Cum sociis natoque penatibus et magnis dis parturient montes, nascetur ridiculus mus. Donec quam felis, ultricies nec, pellentesque eu, pretium quis, sem. Nulla consequat massa quis enim. Donec pede justo, fringilla vel, aliquet nec, vulputate eget, arcu. In enim justo, rhoncus ut, imperdiet a, venenatis vitae, justo. Nullam dictum felis eu pede mollis pretium. Integer tincidunt. Cras dapibus.</p>
  </div>
  <div class="columns col2">
    <h4>Lorem ipsum</h4>
    <p>Vivamus elementum semper nisi. Aenean vulputate eleifend tellus. Aenean leo ligula, porttitor eu, consequat vitae, eleifend ac, enim. Aliquam lorem ante, dapibus in, viverra quis, feugiat a, tellus. Phasellus viverra nulla ut metus varius laoreet. Quisque rutrum. Aenean imperdiet. Etiam ultricies nisi vel augue. Curabitur ullamcorper ultricies nisi. Nam eget dui. Etiam rhoncus. Maecenas tempus, tellus eget condimentum rhoncus, sem quam semper libero, sit amet adipiscing sem neque sed ipsum.</p>
    <h4>Lorem ipsum</h4>
    <p>Nam quam nunc, blandit vel, luctus pulvinar, hendrerit id, lorem. Maecenas nec odio et ante tincidunt tempus. Donec vitae sapien ut libero venenatis faucibus. Nullam quis ante. Etiam sit amet orci eget eros faucibus tincidunt. Duis leo</p>
  </div>
  <div class="columns col3">
    <h4>Lorem ipsum</h4>
    <p>Lorem ipsum dolor sit amet, consectetuer adipiscing elit. Aenean commodo ligula eget dolor. Aenean massa. Cum sociis natoque penatibus et magnis dis parturient montes, nascetur ridiculus mus. Donec quam felis, ultricies nec, pellentesque eu, pretium quis, sem. Nulla consequat massa quis enim. Donec pede justo, fringilla vel, aliquet nec, vulputate eget, arcu. In enim justo, rhoncus ut, imperdiet a, venenatis vitae, justo. Nullam dictum felis eu pede mollis pretium. Integer tincidunt. Cras dapibus.</p>
    <h4>Lorem ipsum</h4>
    <p>Vivamus elementum semper nisi. Aenean vulputate eleifend tellus. Aenean leo ligula, porttitor eu, consequat vitae, eleifend ac, enim. Aliquam lorem ante, dapibus in, viverra quis, feugiat a, tellus. Phasellus viverra nulla ut metus varius laoreet.</p>
  </div>
  <div class="columns col4">
    <p>Quisque rutrum. Aenean imperdiet. Etiam ultricies nisi vel augue. Curabitur ullamcorper ultricies nisi. Nam eget dui. Etiam rhoncus. Maecenas tempus, tellus eget condimentum rhoncus, sem quam semper libero, sit amet adipiscing sem neque sed ipsum.</p>
    <h4>Lorem ipsum</h4>
    <p>Nam quam nunc, blandit vel, luctus pulvinar, hendrerit id, lorem. Maecenas nec odio et ante tincidunt tempus. Donec vitae sapien ut libero venenatis faucibus. Nullam quis ante. Etiam sit amet orci eget eros faucibus tincidunt. Duis leo</p>
  </div>
</section>

<section class="panel back-single">
  <svg class="bg-shapes" viewBox="0 0 378 378" preserveAspectRatio="none">
    <polygon points="118,378 378,260 378,378" fill="var(--white)"/>
  </svg>
  <div class="brand-block">
    <div class="brand-name">Lumen Immobilien GmbH</div>
    <div class="brand-rule"></div>
    <div class="slogan">Besser wohnen – Besser leben!</div>
    <div class="office main">
      <h3>HAUPTGESCHÄFTSSTELLE NORDHEIM</h3>
      <p>Lumen Immobilien GmbH</p>
      <p>Lindenweg 7<br>21000 Nordheim<br>info@lumen-immobilien.example<br>Tel.&nbsp; +49 4100-1 23 45 60<br>Fax. +49 4100-1 23 45 61</p>
    </div>
    <div class="office branch">
      <h3>FILIALE SÜDHAFEN</h3>
      <p>Lumen Immobilien GmbH</p>
      <p>Hafenweg 35<br>21600 Südhafen<br>suedhafen@lumen-immobilien.example<br>Tel.&nbsp; +49 4160-9 87 65 40<br>Fax. +49 4160-9 87 65 41</p>
    </div>
  </div>
</section>

</body>
</html>
```